Construction Company business card and Logo.

We need a business card for a Building Company.
We build and constuction manage.
A simple logo is also required. Ive attached some samples that may assist.
Logo colours: Blue,sunburnt orange,lime/green and brown/grey.
The Font for the Brevanta logo ive been using is Georgia.
Maybe the A in Brevanta can be like my logo design..?
All other font either calibri or arial, something simple.
Simple/modern and neat is what i am looking for.
My card should look organised to convey what the company is about.

Target Market(s)

Developers, architects, proffesionals in general

Industry/Entity Type

Business

Contact Information for Business Card

Brevanta Constructions Pty Ltd
ACN: 381 607 925 Lic:716382D
Dermot Halvorsen
Managing Director
0438 215 706
dermot@brevanta.com.au
www.brevanta.com.au
Industrial.Commercial.Residential.Build Management

Requirements
Must have
• Ive attached some ideas for the logo. Its simple. If you come up with something else, please show me as im not 100% sure of what i want.
The front of the card should be white.
The back of the card should have the company name and logo with Blue background
Should not have
• the design should be simple.
No old style fonts or italics etc

```html
<!DOCTYPE html>
<html lang="en">
<head>
<meta charset="utf-8">
<title>Brevanta Construction Pty Ltd – Business Card</title>
<link rel="stylesheet" href="https://fonts.googleapis.com/css2?family=Arimo:wght@400;700&display=swap">
<style>
  :root {
    --backdrop: #2b2b2b;
    --card-white: #f4f4f4;
    --brand-blue: #1a6fc0;
    --brand-blue-light: #1f8ddb;
    --brand-blue-dark: #0f4f98;
    --brand-orange: #f0962a;
    --ink: #1a1a1a;
    --ink-soft: #3a3a3a;
    --white: #ffffff;
  }
  * { box-sizing: border-box; margin: 0; padding: 0; }
  html, body { width: 1200px; height: 900px; overflow: hidden; }
  body {
    background: var(--backdrop);
    font-family: "Arimo", Arial, sans-serif;
    position: relative;
  }
  .card {
    position: absolute;
    width: 560px;
    height: 320px;
    left: 320px;
    overflow: hidden;
    box-shadow: 0 10px 30px rgba(0,0,0,0.45);
  }

  /* Front */
  .card-front { top: 70px; background: var(--card-white); }
  .front-logo {
    position: absolute; left: 48px; top: 70px;
    display: flex; align-items: center; gap: 12px;
  }
  .logo-square { width: 30px; height: 30px; background: var(--brand-blue); }
  .front-logo .wordmark {
    font-size: 42px; font-weight: 400; color: var(--brand-orange); line-height: 1;
  }
  .front-logo .legal {
    position: absolute; left: 42px; top: 46px;
    font-size: 13px; color: var(--ink); white-space: nowrap;
  }
  .person { position: absolute; left: 48px; top: 152px; }
  .person-name { font-size: 19px; font-weight: 700; color: var(--ink); }
  .person-title { font-size: 13px; color: var(--ink-soft); margin-top: 3px; }
  .contacts {
    position: absolute; left: 48px; top: 208px;
    list-style: none; font-size: 13px; color: var(--ink); line-height: 1.5;
  }
  .contacts .label { color: var(--brand-orange); display: inline-block; width: 26px; }
  .front-stripe {
    position: absolute; left: 0; right: 0; bottom: 0; height: 34px;
    background: var(--brand-blue);
  }
  .front-stripe-thin {
    position: absolute; left: 0; right: 0; bottom: 40px; height: 4px;
    background: var(--brand-blue);
  }

  /* Back */
  .card-back {
    top: 480px;
    background: linear-gradient(135deg, var(--brand-blue-light) 0%, var(--brand-blue) 55%, var(--brand-blue-dark) 100%);
    color: var(--white);
  }
  .back-logo {
    position: absolute; left: 70px; top: 82px;
    display: flex; align-items: center; gap: 18px;
  }
  .back-logo .logo-square { width: 52px; height: 52px; background: var(--white); }
  .back-logo .wordmark { font-size: 82px; font-weight: 400; line-height: 1; }
  .back-logo .legal {
    position: absolute; left: 200px; top: 88px;
    font-size: 20px; white-space: nowrap;
  }
  .services {
    position: absolute; left: 40px; right: 40px; bottom: 40px;
    font-size: 15px; letter-spacing: 0.08em; white-space: nowrap;
  }
  .services .divider { margin: 0 8px; }
</style>
</head>
<body>

  <section class="card card-front" aria-label="Business card front">
    <div class="front-logo">
      <span class="logo-square"></span>
      <span class="wordmark">Brevanta</span>
      <span class="legal">Construction Pty Ltd</span>
    </div>
    <div class="person">
      <p class="person-name">Dermot Halvorsen</p>
      <p class="person-title">Construction Manager</p>
    </div>
    <ul class="contacts">
      <li><span class="label">M :</span>0438 215 706</li>
      <li><span class="label">E :</span>dermot@brevanta.com.au</li>
      <li><span class="label">W :</span>www.brevanta.com.au</li>
    </ul>
    <div class="front-stripe-thin"></div>
    <div class="front-stripe"></div>
  </section>

  <section class="card card-back" aria-label="Business card back">
    <div class="back-logo">
      <span class="logo-square"></span>
      <span class="wordmark">Brevanta</span>
      <span class="legal">Construction Pty Ltd</span>
    </div>
    <p class="services">
      INDUSTRIAL<span class="divider">I</span>COMMERCIAL<span class="divider">I</span>RESIDENTIAL<span class="divider">I</span>MANAGEMENT
    </p>
  </section>

</body>
</html>
```